Wedding Program

Miriam and Owen are getting married. They are looking for a simple 4-page program that conveys the special day. Venue is a museum in a large East-Coast city: classic 18th century, formal. Ceremony is non-religious. Party includes a photo booth and DJ.

He's a math geek - she's an activist/educator.

Please incorporate unique design sensibility - be creative! Colors of purple, eggplant, ivory, and gray are the couple's choice. Fall motif OK.

Target Market(s)

ages 25 - 85, members of a family

Industry/Entity Type

Graphic Design

Font styles to use
Serif
Decorative

Colors
8769ae
b7a5cd
fece3e
f78f20
757575
cfcfcf
6b449b
a64599
fffaee

Requirements
Must have
• Readable, attractive 4-color design using the copy and image provided in the attachment.
Nice to have
• It's a LOVE-ly day for a wedding - be creative!
Should not have
• Avoid flowery girly-girl fonts or obvious hearts and flowers stuff.

```html
<!DOCTYPE html>
<html lang="en">
<head>
<meta charset="utf-8">
<title>Miriam &amp; Owen – Wedding Program</title>
<link rel="stylesheet" href="https://fonts.googleapis.com/css2?family=Aleo:wght@300;400;700&display=swap">
<style>
  :root {
    --ivory: #fffaee;
    --card: #fcf8f0;
    --purple: #6b449b;
    --yellow: #fece3e;
    --orange: #f78f20;
    --backdrop: #e6e2da;
    --shadow: rgba(40, 30, 20, 0.28);
  }
  * { margin: 0; padding: 0; box-sizing: border-box; }
  html, body {
    width: 900px; height: 1200px; overflow: hidden;
    background: var(--backdrop);
    font-family: "Aleo", Georgia, serif;
  }
  .program { position: relative; width: 900px; height: 1200px; }

  .page {
    position: absolute; left: 262px; width: 358px;
    background: var(--card);
    box-shadow: 0 5px 9px var(--shadow);
  }
  .cover { top: 243px; height: 485px; z-index: 4; }
  .tab { display: flex; align-items: center; justify-content: center;
         color: var(--yellow); font-weight: 700; font-size: 17px; letter-spacing: 0.2px; text-transform: uppercase; }
  .tab--party { top: 728px; height: 80px; z-index: 3; }
  .tab--processional { top: 808px; height: 75px; z-index: 2; }
  .tab--guests { top: 883px; height: 75px; z-index: 1; }

  .eyelet {
    position: absolute; left: 166px; top: 13px; width: 18px; height: 18px; border-radius: 50%;
    background: #8d8a86; border: 3px solid #c9c6c0;
  }
  .emblem {
    position: absolute; left: 116px; top: 41px; width: 118px; height: 118px;
    border-radius: 50%; background: var(--yellow);
  }

  .invite { position: absolute; left: 0; right: 0; top: 196px; text-align: center; }
  .invite__couple { font-size: 14px; font-weight: 700; color: var(--yellow); line-height: 18px; }
  .invite__couple .and { color: var(--purple); font-weight: 400; }
  .invite__line { font-size: 14px; color: var(--purple); line-height: 18px; }
  .invite__title { font-size: 56px; font-weight: 700; color: var(--purple); line-height: 70px; margin-top: 14px; letter-spacing: 0; }

  .details { position: absolute; top: 345px; left: 0; right: 0; display: flex; justify-content: center; }
  .when { width: 138px; text-align: right; color: var(--purple); padding-right: 8px; }
  .when__day { font-size: 11px; font-weight: 700; letter-spacing: 2px; line-height: 14px; }
  .when__date { font-size: 62px; font-weight: 300; color: var(--yellow); line-height: 58px; letter-spacing: -2px; }
  .when__time { font-size: 11px; font-weight: 700; letter-spacing: 2px; line-height: 14px; }
  .when__note { font-size: 11px; font-weight: 700; line-height: 14px; }
  .divider { width: 2px; height: 112px; margin-top: 2px; background: var(--orange); }
  .where { padding-left: 13px; width: 190px; font-size: 22px; font-weight: 300; color: var(--purple); line-height: 29px; }
</style>
</head>
<body>
<main class="program">
  <section class="page cover">
    <span class="eyelet"></span>
    <div class="emblem" role="img" aria-label="Couple's emblem: yellow round badge with wedding rings"></div>

    <div class="invite">
      <p class="invite__couple">MIRIAM ASHFORD <span class="and">and</span> OWEN DELMONT</p>
      <p class="invite__line">would be delighted to invite you to their</p>
      <h1 class="invite__title">WEDDING</h1>
    </div>

    <div class="details">
      <div class="when">
        <p class="when__day">Saturday<br>November</p>
        <p class="when__date">01</p>
        <p class="when__time">At 6 p.m.</p>
        <p class="when__note">in the evening</p>
      </div>
      <span class="divider"></span>
      <p class="where">The Society<br>of Naturalists<br>Philadelphia<br>Pennsylvania</p>
    </div>
  </section>

  <section class="page tab tab--party">The Wedding Party</section>
  <section class="page tab tab--processional">Processional</section>
  <section class="page tab tab--guests">To Our Wedding Guests</section>
</main>
</body>
</html>
```